Civil engineering company | Billboard

We need a billboard design for Velmora- civil engineering company. We want big logo in the center of billboard and web site (www.velmora.hr) below the logo. Also, we want an subtle abstract pattern in the background. Dimensions of the billboard are: width :10 m, height: 2m. Design must be celan and modern.
Industry/Entity Type
Civil engineering
Font styles to use
Sans Serif
Colors
F0912C
F2A743
F7CA91
FBE8D2
FDF5EE
Requirements
Must have
- Logo and new unique pattern design for Velmroa company
Should not have
- pictures of construction machinery and tools

```html
<!DOCTYPE html>
<html lang="hr">
<head>
<meta charset="utf-8">
<title>Velmora – billboard</title>
<link rel="stylesheet" href="https://fonts.googleapis.com/css2?family=Quicksand:wght@600;700&family=Raleway:wght@700&display=swap">
<style>
  :root {
    --page-bg: #f3f3f1;
    --cream: #fdf5ee;
    --cream-deep: #fbe8d2;
    --orange: #e8913a;
    --grey: #636363;
    --white: #ffffff;
  }
  * { margin: 0; padding: 0; box-sizing: border-box; }
  html, body {
    width: 1200px;
    height: 1152px;
    overflow: hidden;
    background: var(--page-bg);
  }
  .canvas {
    position: relative;
    width: 1200px;
    height: 1152px;
    display: flex;
    align-items: center;
    justify-content: center;
  }
  .billboard {
    position: relative;
    width: 1200px;
    height: 240px;
    background: var(--cream);
    box-shadow: 0 2px 10px rgba(0,0,0,0.08);
  }
  .billboard__pattern {
    position: absolute;
    inset: 0 0 36px 0;
    background: linear-gradient(90deg, var(--cream-deep) 0%, var(--cream) 22%, var(--white) 50%, var(--cream) 78%, var(--cream-deep) 100%);
  }
  .brand-frame {
    position: absolute;
    left: 145px;
    top: 16px;
    width: 178px;
    height: 178px;
    border: 4px solid var(--grey);
  }
  .brand-name {
    position: absolute;
    left: 346px;
    top: 20px;
    font-family: "Quicksand", sans-serif;
    font-weight: 700;
    font-size: 100px;
    line-height: 1;
    letter-spacing: 6px;
    color: var(--orange);
    text-transform: uppercase;
  }
  .tagline {
    position: absolute;
    left: 350px;
    top: 140px;
    font-family: "Raleway", sans-serif;
    font-weight: 700;
    font-size: 27px;
    line-height: 1;
    letter-spacing: 0.3px;
    color: var(--grey);
    white-space: nowrap;
  }
  .web-strip {
    position: absolute;
    left: 0;
    right: 0;
    bottom: 0;
    height: 36px;
    background: var(--grey);
    display: flex;
    align-items: center;
    justify-content: center;
  }
  .web-strip__url {
    font-family: "Quicksand", sans-serif;
    font-weight: 700;
    font-size: 20px;
    letter-spacing: 1px;
    color: var(--white);
  }
</style>
</head>
<body>
  <main class="canvas">
    <section class="billboard">
      <div class="billboard__pattern" role="img" aria-label="Subtle cream chevron zigzag background pattern"></div>
      <div class="brand-frame"></div>
      <h1 class="brand-name">Velmora</h1>
      <p class="tagline">IZVOĐENJE I VOĐENJE GRAĐEVINSKIH RADOVA</p>
      <div class="web-strip">
        <span class="web-strip__url">www.velmora.hr</span>
      </div>
    </section>
  </main>
</body>
</html>
```